Tavenorix - world unique technology for better life - please let them know who am i at first sight

We need a new business card for company which is a provider of unique crystal based technology suitable for all living being. For more information and final design you can use our brochure (our colours are black and blue from brochure).
We use Verdana font

Industry/Entity Type

Business

Contact Information for Business Card

regular dimension

Font styles to use
Other font styles liked:
• Verdana

Requirements
Must have
• Logo
• name
• function/position
• phone
• mobile
• e-mail
• adress
Nice to have
• inovative design (technology directed)

```html
<!DOCTYPE html>
<html lang="en">
<head>
<meta charset="utf-8">
<title>Tavenorix – Business Card</title>
<link href="https://fonts.googleapis.com/css2?family=Exo+2:wght@400;600&display=swap" rel="stylesheet">
<style>
  :root {
    --blue: #2ba7e1;
    --blue-deep: #1e95cf;
    --white: #ffffff;
    --paper: #f6f7f8;
    --curve-grey: #b8bcc1;
    --stage: #e6e8eb;
    --ink-soft: #eaf6fd;
  }
  * { margin: 0; padding: 0; box-sizing: border-box; }
  html, body {
    width: 1200px; height: 899px; overflow: hidden;
    background: var(--stage);
    font-family: "Exo 2", sans-serif;
  }
  .sheet {
    position: relative; width: 1200px; height: 899px;
    display: flex; align-items: center; justify-content: center; gap: 40px;
  }
  .card {
    position: relative; width: 540px; height: 309px;
    border-radius: 30px; overflow: hidden;
    background: var(--blue);
    box-shadow: 0 10px 30px rgba(0,0,0,.12);
  }
  .card__shape { position: absolute; inset: 0; }

  .brand {
    position: absolute; display: flex; align-items: center; gap: 10px;
    font-weight: 400; letter-spacing: 2px;
  }
  .brand__dot { width: 30px; height: 30px; border-radius: 50%; }
  .brand__name { font-size: 30px; line-height: 1; }

  .card--front .brand { left: 34px; top: 92px; }
  .card--front .brand__dot { background: var(--blue); }
  .card--front .brand__name { color: var(--blue); }

  .person { position: absolute; left: 330px; top: 56px; color: var(--white); }
  .person__name { font-size: 15px; font-weight: 600; letter-spacing: 1px; }
  .person__role { font-size: 11px; margin-top: 2px; }

  .address {
    position: absolute; left: 330px; top: 120px;
    color: var(--white); font-size: 12px; line-height: 1.45;
  }

  .contacts {
    position: absolute; left: 300px; top: 186px;
    list-style: none; color: var(--white); font-size: 9.5px;
  }
  .contacts li { display: flex; align-items: center; gap: 8px; height: 18px; }
  .contacts svg { width: 11px; height: 11px; fill: var(--white); flex: none; }

  .card--back .brand { left: 50%; top: 50%; transform: translate(-50%, -50%); }
  .card--back .brand__dot { background: var(--white); }
  .card--back .brand__name { color: var(--white); font-size: 34px; }
</style>
</head>
<body>
<main class="sheet">

  <section class="card card--front" aria-label="Business card front">
    <svg class="card__shape" viewBox="0 0 540 309" aria-hidden="true">
      <path d="M0,0 H338 C298,46 322,214 164,252 C108,264 44,268 0,270 Z" fill="var(--curve-grey)"/>
      <path d="M0,0 H322 C282,40 304,200 152,240 C100,253 40,257 0,260 Z" fill="var(--paper)"/>
    </svg>

    <div class="brand">
      <span class="brand__dot"></span>
      <span class="brand__name">TAVENORIX</span>
    </div>

    <div class="person">
      <p class="person__name">MAREK DELVAINE</p>
      <p class="person__role">Managing Director</p>
    </div>

    <p class="address">27 Orion Park, 4th floor<br>Keller Street QTN</p>

    <ul class="contacts">
      <li>
        <svg viewBox="0 0 24 24"><path d="M6.6 10.8a15 15 0 0 0 6.6 6.6l2.2-2.2a1 1 0 0 1 1-.25 11.4 11.4 0 0 0 3.6.57 1 1 0 0 1 1 1V20a1 1 0 0 1-1 1A17 17 0 0 1 3 4a1 1 0 0 1 1-1h3.5a1 1 0 0 1 1 1c0 1.25.2 2.45.57 3.6a1 1 0 0 1-.25 1z"/></svg>
        <span>014 627 3850</span>
      </li>
      <li>
        <svg viewBox="0 0 24 24"><path d="M7 1h10a2 2 0 0 1 2 2v18a2 2 0 0 1-2 2H7a2 2 0 0 1-2-2V3a2 2 0 0 1 2-2zm0 3v14h10V4zm5 15.2a1.2 1.2 0 1 0 0 2.4 1.2 1.2 0 0 0 0-2.4z"/></svg>
        <span>014 627 3851</span>
      </li>
      <li>
        <svg viewBox="0 0 24 24"><path d="M6 2h9v5H6zM3 8h18a1 1 0 0 1 1 1v10a1 1 0 0 1-1 1H3a1 1 0 0 1-1-1V9a1 1 0 0 1 1-1zm3 4v2h6v-2z"/></svg>
        <span>014 627 3852</span>
      </li>
      <li>
        <svg viewBox="0 0 24 24"><path d="M2 5h20v14H2zm2 2v.5l8 5 8-5V7zm0 3v7h16v-7l-8 5z"/></svg>
        <span>hello@tavenorix.com</span>
      </li>
      <li>
        <svg viewBox="0 0 24 24"><path d="M12 2a10 10 0 1 0 0 20 10 10 0 0 0 0-20zm6.9 6h-3a15 15 0 0 0-1.3-3.9A8 8 0 0 1 18.9 8zM12 4c.8 1.2 1.5 2.5 1.9 4h-3.8c.4-1.5 1.1-2.8 1.9-4zM4.3 14a8 8 0 0 1 0-4h3.4a16 16 0 0 0 0 4zm.8 2h3a15 15 0 0 0 1.3 3.9A8 8 0 0 1 5.1 16zm3-8h-3a8 8 0 0 1 4.3-3.9A15 15 0 0 0 8.1 8zM12 20c-.8-1.2-1.5-2.5-1.9-4h3.8c-.4 1.5-1.1 2.8-1.9 4zm2.3-6H9.7a14 14 0 0 1 0-4h4.6a14 14 0 0 1 0 4zm.3 5.9a15 15 0 0 0 1.3-3.9h3a8 8 0 0 1-4.3 3.9zm1.7-5.9a16 16 0 0 0 0-4h3.4a8 8 0 0 1 0 4z"/></svg>
        <span>www.tavenorix.com</span>
      </li>
    </ul>
  </section>

  <section class="card card--back" aria-label="Business card back">
    <div class="brand">
      <span class="brand__dot"></span>
      <span class="brand__name">TAVENORIX</span>
    </div>
  </section>

</main>
</body>
</html>
```